Humorous Book by Comedian Needs E-book Cover

My book 'A Lantern on the Porch' is on Pagewick but I want a better cover designed. Cover needs my photo on it. My name is the most important text (because I have an existing audience.)

Text elements:
Author: Dorvel Quint
Title: A Lantern on the Porch
Subtitle: Tenth Anniversary Edition
Review Quote: 'All of his columns are amusing. The best are masterpieces.' Harbour Ledger

Above my name it should say: Collected Humour From NZ's Award-Winning Comedian

Here's the present version (which is why I want an improved version!)
http://www.shelvora-books.example/Lantern-Porch-Tenth-Edition-ebook/dp/Q73ZT9X418

Book covers I admire:

http://www.shelvora-books.example/Why-I-Left-Verna-Holcott-ebook/dp/Q2281MV7LD/ref=shv_pw_title_0

http://www.shelvora-books.example/Grumblecoat-Prue-Odell-ebook/dp/Q903JXN517/ref=shv_pw_title_0

http://www.shelvora-books.example/Say-Yes-Later-Neil-Fratten-ebook/dp/Q41RD8EL3K

Pagewick covers need to work as thumbnails, as well as on small device screens.

This cover is for Marlowe Pagewick. Tech specs are on Pagewick Self Release page. Dimensions: Requirements for the size of your cover art have an ideal height/width ratio of 1.6, this means: • A minimum of 625 pixels on the shortest side and 1000 pixels on the longest side • For best quality, your image would be 2820 pixels on the shortest side and 4500 pixels on the longest side

Dimensions Requirements for the size of your cover art have an ideal height/width ratio of 1.6, this means: • A minimum of 625 pixels on the shortest side and 1000 pixels on the longest side • For best quality, your image would be 2820 pixels on the shortest side and 4500 pixels on the longest side

```html
<!DOCTYPE html>
<html lang="en">
<head>
<meta charset="utf-8">
<title>A Lantern on the Porch – Dorvel Quint</title>
<link href="https://fonts.googleapis.com/css2?family=Oswald:wght@400;500;600&family=Roboto+Condensed:ital,wght@0,700;1,400&family=Sue+Ellen+Francisco&display=swap" rel="stylesheet">
<style>
  :root {
    --lime: #d9ec1c;
    --lime-light: #eef52e;
    --pink: #e8336b;
    --pink-dark: #c91f55;
    --olive: #a7a41a;
    --sky: #3ec4dc;
    --teal: #1d8793;
    --rule-red: #d8344a;
    --quote-blue: #1a78a6;
    --white: #ffffff;
  }
  * { margin: 0; padding: 0; box-sizing: border-box; }
  html, body { width: 752px; height: 1200px; overflow: hidden; background: #ffffff; }
  .cover {
    position: relative;
    width: 752px;
    height: 1200px;
    overflow: hidden;
    background: radial-gradient(ellipse at 55% 45%, var(--lime-light) 0%, var(--lime) 60%, #cfe316 100%);
    font-family: "Oswald", sans-serif;
  }
  .tagline {
    position: absolute;
    left: 0; top: 35px;
    width: 752px; height: 44px;
    background: var(--pink);
    border-bottom: 7px solid var(--olive);
    color: var(--white);
    font-family: "Roboto Condensed", sans-serif;
    font-weight: 700;
    font-size: 24px;
    line-height: 38px;
    text-align: center;
    letter-spacing: 0.2px;
  }
  .author {
    position: absolute;
    left: 20px; top: 112px;
    width: 712px;
    font-weight: 500;
    font-size: 116px;
    line-height: 150px;
    letter-spacing: 3px;
    text-align: center;
    white-space: nowrap;
  }
  .author-first { color: var(--sky); }
  .author-last { color: var(--teal); }
  .name-rule {
    position: absolute;
    left: 63px; top: 281px;
    width: 620px; height: 2px;
    background: var(--rule-red);
  }
  .author-photo {
    position: absolute;
    left: 0; top: 312px;
    width: 515px; height: 888px;
    border-radius: 46% 50% 0 0 / 22% 22% 0 0;
    background: linear-gradient(180deg, #4a3a30 0%, #d7a984 14%, #e8c2a0 26%, #f2f0ec 34%, var(--pink) 42%, var(--pink-dark) 100%);
    opacity: 0.95;
  }
  .title {
    position: absolute;
    left: 300px; top: 385px;
    width: 430px;
    font-family: "Sue Ellen Francisco", cursive;
    font-weight: 400;
    font-size: 104px;
    line-height: 110px;
    color: var(--teal);
    text-align: center;
  }
  .review {
    position: absolute;
    right: 35px; top: 850px;
    width: 190px;
    text-align: right;
    color: var(--quote-blue);
  }
  .review-quote {
    font-family: "Roboto Condensed", sans-serif;
    font-style: italic;
    font-weight: 400;
    font-size: 28px;
    line-height: 38px;
    white-space: nowrap;
    direction: rtl;
    unicode-bidi: plaintext;
  }
  .review-source {
    font-family: "Roboto Condensed", sans-serif;
    font-weight: 700;
    font-size: 27px;
    line-height: 40px;
    margin-top: 4px;
    white-space: nowrap;
  }
  .edition {
    position: absolute;
    left: 0; top: 1109px;
    width: 752px; height: 40px;
    background: var(--sky);
    border-top: 2px solid var(--white);
    color: var(--white);
    font-family: "Oswald", sans-serif;
    font-weight: 400;
    font-size: 21px;
    line-height: 37px;
    letter-spacing: 5px;
    text-align: center;
  }
</style>
</head>
<body>
  <div class="cover">
    <div class="tagline">COLLECTED HUMOUR FROM NZ'S AWARD-WINNING COMEDIAN</div>
    <div class="author-photo" role="img" aria-label="Portrait of the author smiling in glasses, a pink jacket and a bow tie"></div>
    <h1 class="author"><span class="author-first">DORVEL</span><span class="author-last">QUINT</span></h1>
    <div class="name-rule"></div>
    <h2 class="title">A Lantern<br>on the Porch</h2>
    <blockquote class="review">
      <p class="review-quote">All of his columns<br>are amusing.<br>The best are<br>masterpieces.'</p>
      <p class="review-source">HARBOUR LEDGER</p>
    </blockquote>
    <div class="edition">TENTH ANNIVERSARY EDITION</div>
  </div>
</body>
</html>
```